I want a double sided flyer possibly with a picture of a lawn or grass.
Company name, phone number, email, and logo
Halvorsen Turf Management, (404)726-1853,Halvorsen_Turf@brevimail.com
Company services
Fertilization and weed control,Lawn and Landscape maintenance, mowing, pruning, aeration, landscape and Christmas lights,

```html
<!DOCTYPE html>
<html lang="en">
<head>
<meta charset="UTF-8">
<title>Halvorsen Turf Management – Flyer</title>
<link href="https://fonts.googleapis.com/css2?family=Oswald:wght@400;600&family=PT+Sans:wght@400;700&display=swap" rel="stylesheet">
<style>
  :root {
    --stage: #e6e7e8;
    --grass-deep: #2f7d12;
    --grass-mid: #5aa51c;
    --grass-light: #b9dc4a;
    --brand-green: #3c9a1e;
    --ink: #3a3d3f;
    --rule: #bfc3c5;
    --paper: #ffffff;
  }
  * { box-sizing: border-box; margin: 0; padding: 0; }
  html, body { width: 1200px; height: 800px; overflow: hidden; }
  body {
    background: var(--stage);
    font-family: "PT Sans", Arial, sans-serif;
    position: relative;
  }
  .flyer {
    position: absolute;
    top: 210px;
    width: 560px;
    height: 380px;
    overflow: hidden;
    box-shadow: 0 6px 18px rgba(0,0,0,.18);
  }
  .flyer--front { left: 30px; background: var(--paper); }
  .flyer--back { left: 610px; }

  /* front */
  .front-photo {
    position: absolute; inset: 0 0 56px 0;
    background:
      linear-gradient(200deg, rgba(255,255,255,.95) 0%, rgba(255,255,255,.75) 38%, rgba(255,255,255,0) 70%),
      linear-gradient(10deg, var(--grass-deep) 0%, var(--grass-mid) 35%, var(--grass-light) 65%, #eef5d8 100%);
  }
  .headline {
    position: absolute; left: 34px; top: 22px;
    font-family: "Oswald", "Arial Narrow", sans-serif;
    font-weight: 600; text-transform: uppercase;
    color: var(--ink); line-height: .95;
  }
  .headline span { display: block; }
  .headline .hl-we { font-size: 30px; }
  .headline .hl-care { font-size: 46px; }
  .headline .hl-for { font-size: 26px; font-weight: 400; }
  .headline .hl-yard { font-size: 48px; color: var(--brand-green); }
  .headline-rule {
    position: absolute; left: 200px; top: 110px;
    width: 8px; height: 192px; background: var(--brand-green);
  }
  .services {
    position: absolute; left: 208px; top: 110px;
    width: 320px; height: 192px;
    background: rgba(255,255,255,.9);
    padding: 14px 20px;
  }
  .services h2 {
    font-family: "Oswald", "Arial Narrow", sans-serif;
    font-weight: 400; font-size: 20px; line-height: 1.2;
    color: var(--brand-green); text-transform: uppercase;
    margin-bottom: 8px;
  }
  .services ul { list-style: none; }
  .services li {
    font-size: 14px; color: var(--ink); line-height: 1.4;
    padding-left: 16px; position: relative; white-space: nowrap;
  }
  .services li::before {
    content: ""; position: absolute; left: 2px; top: 8px;
    width: 6px; height: 6px; border-radius: 50%; background: var(--brand-green);
  }
  .contact-strip {
    position: absolute; left: 0; right: 0; bottom: 0; height: 56px;
    display: flex; align-items: stretch; background: var(--paper);
  }
  .company-tab {
    background: var(--brand-green); color: var(--paper);
    font-size: 12px; display: flex; align-items: center;
    padding: 0 12px; flex: 0 0 auto; white-space: nowrap;
  }
  .contact-list {
    flex: 1 1 auto;
    display: flex; align-items: center; justify-content: space-between; gap: 10px;
    padding: 0 12px; font-size: 12px; color: var(--ink); white-space: nowrap;
  }
  .contact-item { display: flex; align-items: center; gap: 6px; }
  .contact-divider { width: 1px; height: 26px; background: var(--rule); flex: 0 0 1px; }
  .contact-phone { font-size: 15px; }

  /* back */
  .back-turf {
    position: absolute; inset: 0;
    background: radial-gradient(ellipse at 50% 45%, #4fa520 0%, #3b8e16 55%, #2a6d0e 100%);
  }
  .back-name {
    position: absolute; left: 0; right: 0; top: 50%;
    transform: translateY(-50%);
    text-align: center;
    font-family: "PT Sans", Arial, sans-serif;
    font-weight: 700; font-size: 30px;
    color: #24600b; text-transform: uppercase; letter-spacing: 1px;
  }
</style>
</head>
<body>

<section class="flyer flyer--front" aria-label="Flyer front">
  <div class="front-photo" role="img" aria-label="Close-up photo of fresh green grass with soft light"></div>

  <h1 class="headline">
    <span class="hl-we">We</span>
    <span class="hl-care">Care</span>
    <span class="hl-for">For your</span>
    <span class="hl-yard">Yard!</span>
  </h1>

  <div class="headline-rule"></div>
  <div class="services">
    <h2>Company Services</h2>
    <ul>
      <li>Fertilization and weed control</li>
      <li>Lawn and Landscape maintenance</li>
      <li>Mowing</li>
      <li>Pruning</li>
      <li>Aeration</li>
      <li>Landscape and Christmas lights</li>
    </ul>
  </div>

  <footer class="contact-strip">
    <div class="company-tab">Halvorsen Turf Management</div>
    <div class="contact-list">
      <span class="contact-item">
        <svg width="16" height="12" viewBox="0 0 18 14" aria-hidden="true">
          <rect x="1" y="1" width="16" height="12" fill="none" stroke="#3a3d3f" stroke-width="1.5"/>
          <path d="M1 1 L9 8 L17 1 M1 13 L7 7 M17 13 L11 7" fill="none" stroke="#3a3d3f" stroke-width="1.5"/>
        </svg>
        Halvorsen_Turf@brevimail.com
      </span>
      <span class="contact-divider"></span>
      <span class="contact-item contact-phone">
        <svg width="18" height="18" viewBox="0 0 20 20" aria-hidden="true">
          <circle cx="10" cy="10" r="9" fill="none" stroke="#3c9a1e" stroke-width="1.6"/>
          <path d="M7 5.5 L8.8 8 L7.8 9.2 Q9 11.4 10.8 12.2 L12 11.2 L14.5 13 L13.4 14.6 Q9.5 14.6 6.4 10.4 Q5.4 8 6 6.4 Z" fill="#3c9a1e"/>
        </svg>
        (404)726-1853
      </span>
    </div>
  </footer>
</section>

<section class="flyer flyer--back" aria-label="Flyer back">
  <div class="back-turf" role="img" aria-label="Full-bleed texture of dense green lawn grass"></div>
  <p class="back-name">Halvorsen Turf Management</p>
</section>

</body>
</html>
```